HR consultancy website - Wordpress Design Project

We need a wordpress design for a new company based in Belgium called Brivoltex. We propose HR consultancy services focused on employees' engagement (motivation). We target corporations from 100 to 1000+ employees mainly in Europe.
We need a new design for our existing website (www.brivoltex.eu).
We find the current design too static and outdated and we are looking for a more appealing look & feel.
Nevertheless, it has also to be sober.
The colours of the logo (dark blue, purple and light grey) should be preferrably used.
The content structure and the texts remain the same.

Target Market(s)

HR managers, general managers of SME's, higher education

Industry/Entity Type

It Company

Requirements
Must have
• No specific functionalities, except a contact form.

```html
<!DOCTYPE html>
<html lang="en">
<head>
<meta charset="utf-8">
<title>Brivoltex — Employee Engagement</title>
<link rel="stylesheet" href="https://fonts.googleapis.com/css2?family=Bree+Serif&family=Montserrat:wght@300;400&family=PT+Serif&display=swap">
<style>
:root{
  --pink:#d02a74;
  --pink-dark:#b81f63;
  --blue:#0c5fae;
  --blue-dark:#064a8e;
  --grey-logo:#cdc6c0;
  --text:#5a5654;
  --heading:#6b6662;
  --footer:#a3968b;
  --band:#121212;
  --rule:#dcdcdc;
}
*{box-sizing:border-box;margin:0;padding:0}
html,body{width:1200px;height:1013px;overflow:hidden;background:#fff}
body{position:relative;font-family:"Montserrat",sans-serif;color:var(--text)}
.top-rule{position:absolute;left:0;top:0;width:1200px;height:4px;background:var(--pink)}
.brand{position:absolute;left:140px;top:26px;font-family:"Montserrat",sans-serif;font-weight:400;font-size:54px;letter-spacing:1px;color:var(--grey-logo);line-height:1}
.main-nav{position:absolute;top:4px;right:130px;display:flex;height:32px}
.main-nav a{display:block;padding:0 20px;line-height:32px;font-size:17px;color:#222;text-decoration:none;margin-left:16px}
.main-nav a.active{background:var(--pink);color:#fff;margin-left:0}
.hero-band{position:absolute;left:0;top:110px;width:1200px;height:360px;background:var(--band)}
.page-glow{position:absolute;left:0;top:470px;width:1200px;height:260px;background:linear-gradient(#ececec,#fff)}
.hero-frame{position:absolute;left:140px;top:130px;width:920px;height:367px;background:#fff;border:1px solid #ddd;padding:9px 10px}
.hero-photo{position:absolute;left:10px;top:9px;width:900px;height:349px;background:linear-gradient(180deg,#f4f4f6 0%,#e6e6ea 45%,#c9ccd2 75%,#b8bcc3 100%)}
.hero-caption{position:absolute;left:10px;top:273px;width:900px;height:85px;background:rgba(255,255,255,.72);display:flex;align-items:center}
.hero-name{width:250px;padding-left:14px;font-family:"Bree Serif",serif;font-size:43px;color:var(--pink);border-right:1px solid rgba(0,0,0,.12);height:85px;line-height:85px}
.hero-tagline{padding-left:18px;font-family:"PT Serif",serif;font-size:21px;color:#111;flex:1}
.hero-btn{margin-right:10px;background:var(--pink);color:#fff;font-family:"Bree Serif",serif;font-size:21px;padding:5px 12px;border-radius:18px}
.features{position:absolute;left:140px;top:514px;width:920px;height:212px;display:flex}
.feature{width:233px;position:relative;padding-top:22px}
.feature+.feature{border-left:1px solid #e2e2e2}
.feature:first-child{width:226px}
.ribbon{position:relative;height:46px;margin-left:0;width:217px}
.feature+.feature .ribbon{margin-left:7px}
.ribbon-bar{position:absolute;left:14px;top:2px;width:203px;height:42px;background:linear-gradient(var(--blue),var(--blue-dark));clip-path:polygon(0 0,93% 0,100% 50%,93% 100%,0 100%)}
.ribbon-num{position:absolute;left:0;top:1px;width:44px;height:44px;border-radius:50%;background:var(--blue-dark);border:3px solid #fff;box-shadow:0 0 0 1px #c8d4e2;color:#fff;font-size:24px;text-align:center;line-height:38px}
.ribbon-title{position:absolute;left:56px;top:0;line-height:46px;font-family:"Bree Serif",serif;font-size:28px;color:#fff}
.feature p{margin-top:22px;padding:0 12px;text-align:center;font-size:15.4px;line-height:20.5px;color:var(--text)}
.cta{position:absolute;left:140px;top:772px;width:920px;height:180px;background:radial-gradient(ellipse at 50% 0%,#f0f0f0 0%,#fff 70%);text-align:center}
.cta h2{margin-top:30px;font-family:"Bree Serif",serif;font-weight:400;font-size:25px;color:var(--heading)}
.cta-btn{display:block;margin:24px auto 0;width:219px;height:68px;border-radius:24px;background:linear-gradient(#6a6a6a 0%,#2a2a2a 45%,#050505 55%,#1a1a1a 100%);box-shadow:0 3px 4px rgba(0,0,0,.25);border:2px solid #cfcfcf;color:#fff;font-family:"Bree Serif",serif;font-size:25px;line-height:64px;text-decoration:none}
.site-footer{position:absolute;left:140px;top:958px;width:920px;border-top:1px solid var(--rule);text-align:center;padding-top:15px;font-size:15.5px;color:var(--footer)}
</style>
</head>
<body>
<div class="top-rule"></div>
<header>
  <div class="brand">Brivoltex</div>
  <nav class="main-nav">
    <a class="active" href="#">Our Mission</a>
    <a href="#">About</a>
    <a href="#">Contact</a>
  </nav>
</header>
<div class="hero-band"></div>
<div class="page-glow"></div>
<section class="hero-frame">
  <div class="hero-photo" role="img" aria-label="Team of business professionals in an office, led by a smiling manager"></div>
  <div class="hero-caption">
    <div class="hero-name">Brivoltex</div>
    <div class="hero-tagline">FOSTER PERFORMANCE BY ENGAGING EMPLOYEES</div>
    <div class="hero-btn">Our Mission</div>
  </div>
</section>
<section class="features">
  <div class="feature">
    <div class="ribbon"><div class="ribbon-bar"></div><div class="ribbon-num">1</div><div class="ribbon-title">Evaluation</div></div>
    <p>Only between 13 and 21% of employees are actively engaged in their job.</p>
  </div>
  <div class="feature">
    <div class="ribbon"><div class="ribbon-bar"></div><div class="ribbon-num">2</div><div class="ribbon-title">Strategy</div></div>
    <p>Brivoltex helps corporate leaders get the best contribu­tion from employees.</p>
  </div>
  <div class="feature">
    <div class="ribbon"><div class="ribbon-bar"></div><div class="ribbon-num">3</div><div class="ribbon-title">Process</div></div>
    <p>Our ERM tool creates an HR engagement cycle to encour­age line managers to take ini­tiatives and to enhance the engagement of their team members.</p>
  </div>
  <div class="feature">
    <div class="ribbon"><div class="ribbon-bar"></div><div class="ribbon-num">4</div><div class="ribbon-title">Impact</div></div>
    <p>Our ERM tool measures impact by creating an index which can then be used for comparison over time.</p>
  </div>
</section>
<section class="cta">
  <h2>Boost Your Company's Performance!</h2>
  <a class="cta-btn" href="#">Contact Us</a>
</section>
<footer class="site-footer">Copyright © 2012 Brivoltex. All Rights Reserved.</footer>
</body>
</html>
```